Recruiting ad for Caregivers and Nurses

We need a few amazing, fun, catchy, creative recruiting ads for Caregivers and Nurses to care for homecare patients on the island of Oahu, in Hawaii. We are an in home care company called Brantley Homecare. Our care services are provided 24/7, so we need staff that can work days, nights, weekdays, weekends. We need catchy fun ads to entice caregivers and nurses to call our office to inquire about jobs available. Our patients age range is from babies to seniors. We need caregivers and nurses for basic patient care (bathing, dressing, ambulating, preparing meals, medication reminders, light housekeeping) and complex patients (oxygen, tube feeding, injections, vents, wound care). Here are some bullets to consider including:
*Full-time and Part-time Positions Available (days, nights, weekdays, weekends)
*Sign-On Bonus Programs Offered up to $500
*Refer a Friend Bonus Program
*Holiday Pay
*2 Health Plans to Choose from
*Island-Wide Locations
*All PPE Provided (masks, gloves, etc)
*401K Program
*Tuition Benefits

```html
<!DOCTYPE html>
<html lang="en">
<head>
<meta charset="utf-8">
<title>Brantley Homecare – Hiring Caregivers &amp; Nurses</title>
<link href="https://fonts.googleapis.com/css2?family=Libre+Baskerville:ital,wght@0,400;0,700;1,400&family=Barlow+Semi+Condensed:wght@600;700&family=Barlow:wght@400;500;700&display=swap" rel="stylesheet">
<style>
:root{
  --teal:#127a6e;
  --teal-dark:#0d6659;
  --coral:#f19a80;
  --ink:#1f2326;
  --paper:#ffffff;
  --mist:#e9f0f4;
  --stage:#50565f;
  --scrub:#3f6fc0;
}
*{margin:0;padding:0;box-sizing:border-box}
html,body{width:1200px;height:2452px;overflow:hidden;background:var(--stage)}
.flyer{position:absolute;left:91px;top:102px;width:1018px;height:1315px;overflow:hidden;
  background:linear-gradient(180deg,var(--mist) 0%,#f6f9fb 45%,var(--paper) 60%);
  font-family:"Libre Baskerville",Georgia,serif;color:var(--ink);box-shadow:0 20px 40px rgba(0,0,0,.35)}
.abs{position:absolute;white-space:nowrap}
.photo-nurse{left:560px;top:0;width:458px;height:640px;
  background:linear-gradient(160deg,#dfe6ee 0%,#7fa3d8 35%,var(--scrub) 70%,#2f5aa3 100%)}
.shapes{left:0;top:0;width:1018px;height:1315px}
.brand{left:52px;top:40px;display:flex;align-items:center;gap:14px}
.brand-dot{width:54px;height:54px;border-radius:50%;background:var(--coral)}
.brand-name{font-size:34px;font-weight:400;color:var(--teal);line-height:1.05}
.company{left:55px;top:222px;font-size:21px}
.hiring{left:50px;top:252px;font-size:120px;font-weight:700;color:var(--teal);letter-spacing:-2px;line-height:1}
.rule-hire{left:55px;top:370px;width:580px;height:2px;background:var(--teal)}
.roles{left:55px;top:374px;font-family:"Barlow Semi Condensed",sans-serif;font-weight:700;font-size:61px;color:var(--teal);letter-spacing:.5px;line-height:1.1}
.service{left:57px;top:455px;font-family:"Barlow",sans-serif;font-size:34px;font-weight:400;letter-spacing:.5px;line-height:1.1}
.service b{font-weight:700}
.where{left:57px;top:500px;font-family:"Barlow",sans-serif;font-size:25px;letter-spacing:.5px;line-height:1.1}
.photo-round{border-radius:50%;border:8px solid var(--paper)}
.photo-seniors{left:79px;top:534px;width:300px;height:300px;background:radial-gradient(circle at 40% 40%,#f4e4d8,#8fb7d4 60%,#3a86b8)}
.photo-infant{left:486px;top:466px;width:212px;height:212px;background:radial-gradient(circle at 45% 45%,#f1e0d3,#86c9d6 60%,#2c9db5)}
.positions{left:481px;top:692px;font-size:28px;font-weight:700;color:var(--teal);line-height:1.18}
.shifts{left:481px;top:768px;font-size:17px;letter-spacing:.3px}
.shifts span{color:var(--teal)}
.rule-pos{left:481px;top:802px;width:466px;height:2px;background:#777}
.section-title{font-size:28px;font-weight:700;color:var(--teal);letter-spacing:.5px}
.benefits-title{left:483px;top:832px}
.benefit{display:flex;align-items:center;gap:12px;font-size:17px;line-height:1.15}
.benefit svg{flex:none}
.plans-title{left:67px;top:860px}
.plan-num{width:58px;height:58px;border-radius:50%;background:var(--teal);color:#fff;font-size:30px;display:flex;align-items:center;justify-content:center}
.plan-label{height:27px;background:var(--teal);color:#fff;font-size:17px;padding:0 12px;line-height:27px;width:260px;overflow:hidden}
.plan-desc{font-style:italic;font-size:14.5px;line-height:1.25}
.address{left:85px;top:1172px;font-size:18px;line-height:1.4}
.phone{left:85px;top:1220px;font-family:"Barlow Semi Condensed",sans-serif;font-weight:700;font-size:52px;color:var(--teal);letter-spacing:.5px;line-height:1.1}
.web{left:90px;top:1280px;font-family:"Barlow",sans-serif;font-weight:700;font-size:22px;color:var(--teal);display:flex;align-items:center;gap:8px}
.apply{left:566px;top:1226px;color:#fff}
.apply-lead{font-size:20px}
.apply-mail{font-size:23px;font-weight:700;margin-top:6px}
</style>
</head>
<body>
<main class="flyer">
  <div class="abs photo-nurse" role="img" aria-label="Photo of a nurse in blue scrubs with a stethoscope holding a red clipboard"></div>

  <svg class="abs shapes" viewBox="0 0 1018 1315" aria-hidden="true">
    <path d="M0 585 C130 625 300 665 430 642 C570 616 660 562 1018 555 L1018 612 C820 606 650 646 490 690 C330 730 150 735 0 695 Z" fill="var(--teal)"/>
    <path d="M600 655 C770 598 920 640 1018 705" fill="none" stroke="var(--coral)" stroke-width="12"/>
    <path d="M560 690 C700 650 900 650 1018 720 L1018 900 L560 900 Z" fill="var(--paper)"/>
    <path d="M16 1150 C150 1058 350 1060 520 1115 C700 1162 880 1152 1018 1110 L1018 1315 L470 1315 C440 1222 380 1162 300 1142 C200 1122 100 1130 16 1150 Z" fill="var(--teal)"/>
    <path d="M640 1172 C820 1166 960 1122 1018 1040" fill="none" stroke="var(--coral)" stroke-width="11"/>
  </svg>

  <div class="abs brand"><span class="brand-dot"></span><span class="brand-name">Brantley<br>Homecare</span></div>
  <p class="abs company">Brantley Homecare Company</p>
  <h1 class="abs hiring">HIRING</h1>
  <div class="abs rule-hire"></div>
  <h2 class="abs roles">CAREGIVERS &amp; NURSES</h2>
  <p class="abs service">TO PROVIDE <b>24X7</b> SERVICES</p>
  <p class="abs where">AT THE ISLAND OF OAHU, IN HAWAII</p>

  <div class="abs photo-round photo-seniors" role="img" aria-label="Photo of a smiling caregiver with an elderly woman"></div>
  <div class="abs photo-round photo-infant" role="img" aria-label="Photo of a nurse bottle-feeding a baby"></div>

  <h3 class="abs positions">FULL-TIME AND PART-TIME<br>POSITIONS AVAILABLE</h3>
  <p class="abs shifts"><span>•</span> DAYS <span>•</span> NIGHTS <span>•</span> WEEKDAYS <span>•</span> WEEKENDS</p>
  <div class="abs rule-pos"></div>

  <h3 class="abs section-title benefits-title">KEY BENEFITS</h3>
  <div class="abs benefit" style="left:485px;top:876px">
    <svg width="48" height="48" viewBox="0 0 48 48"><circle cx="24" cy="24" r="22" fill="none" stroke="var(--teal)" stroke-width="2"/><circle cx="24" cy="20" r="7" fill="none" stroke="var(--teal)" stroke-width="2"/><path d="M12 33 H36" stroke="var(--teal)" stroke-width="2"/></svg>
    <span>Sign-On Bonus<br>Programs Offered<br>up to $500</span></div>
  <div class="abs benefit" style="left:485px;top:944px">
    <svg width="48" height="48" viewBox="0 0 48 48"><circle cx="24" cy="24" r="22" fill="none" stroke="var(--teal)" stroke-width="2"/><circle cx="18" cy="20" r="5" fill="none" stroke="var(--teal)" stroke-width="2"/><circle cx="31" cy="27" r="5" fill="none" stroke="var(--teal)" stroke-width="2"/></svg>
    <span>Refer a Friend<br>Bonus Program</span></div>
  <div class="abs benefit" style="left:485px;top:1008px">
    <svg width="48" height="48" viewBox="0 0 48 48"><circle cx="24" cy="24" r="22" fill="none" stroke="var(--teal)" stroke-width="2"/><rect x="14" y="16" width="20" height="16" fill="none" stroke="var(--teal)" stroke-width="2"/><path d="M14 22 H34" stroke="var(--teal)" stroke-width="2"/></svg>
    <span>Holiday Pay</span></div>
  <div class="abs benefit" style="left:485px;top:1070px">
    <svg width="48" height="48" viewBox="0 0 48 48"><circle cx="24" cy="24" r="22" fill="none" stroke="var(--teal)" stroke-width="2"/><rect x="16" y="13" width="16" height="22" fill="none" stroke="var(--teal)" stroke-width="2"/><path d="M24 20 V30 M19 25 H29" stroke="var(--teal)" stroke-width="2"/></svg>
    <span>2 Health Plans to<br>Choose from</span></div>

  <div class="abs benefit" style="left:722px;top:876px">
    <svg width="48" height="48" viewBox="0 0 48 48"><circle cx="24" cy="24" r="22" fill="none" stroke="var(--teal)" stroke-width="2"/><path d="M24 36 C18 28 16 24 16 20 A8 8 0 0 1 32 20 C32 24 30 28 24 36 Z" fill="none" stroke="var(--teal)" stroke-width="2"/><circle cx="24" cy="20" r="3" fill="var(--teal)"/></svg>
    <span>Island-Wide<br>Locations</span></div>
  <div class="abs benefit" style="left:722px;top:944px">
    <svg width="48" height="48" viewBox="0 0 48 48"><circle cx="24" cy="24" r="22" fill="none" stroke="var(--teal)" stroke-width="2"/><circle cx="24" cy="19" r="6" fill="none" stroke="var(--teal)" stroke-width="2"/><path d="M14 35 C15 28 33 28 34 35" fill="none" stroke="var(--teal)" stroke-width="2"/></svg>
    <span>All PPE Provided<br>(masks, gloves, etc)</span></div>
  <div class="abs benefit" style="left:722px;top:1008px">
    <svg width="48" height="48" viewBox="0 0 48 48"><circle cx="24" cy="24" r="22" fill="none" stroke="var(--teal)" stroke-width="2"/><ellipse cx="24" cy="26" rx="11" ry="8" fill="none" stroke="var(--teal)" stroke-width="2"/><path d="M21 16 H27" stroke="var(--teal)" stroke-width="2"/></svg>
    <span>401K Program</span></div>
  <div class="abs benefit" style="left:722px;top:1070px">
    <svg width="48" height="48" viewBox="0 0 48 48"><circle cx="24" cy="24" r="22" fill="none" stroke="var(--teal)" stroke-width="2"/><path d="M12 20 L24 14 L36 20 L24 26 Z" fill="none" stroke="var(--teal)" stroke-width="2"/><path d="M17 23 V30 C20 33 28 33 31 30 V23" fill="none" stroke="var(--teal)" stroke-width="2"/></svg>
    <span>Tuition Benefits</span></div>

  <h3 class="abs section-title plans-title">OUR HEALTH PLANS</h3>
  <div class="abs plan-num" style="left:68px;top:898px">1</div>
  <div class="abs plan-label" style="left:143px;top:904px">BASIC PATIENT CARE</div>
  <p class="abs plan-desc" style="left:147px;top:940px">Bathing, Dressing, Ambulating,<br>Preparing meals, Medication<br>Reminders, Light housekeeping</p>
  <div class="abs plan-num" style="left:68px;top:998px">2</div>
  <div class="abs plan-label" style="left:143px;top:1004px">COMPLEX PATIENTS</div>
  <p class="abs plan-desc" style="left:147px;top:1040px">Oxygen, Tube feeding, Injections,<br>Vents, Wound care.</p>

  <svg class="abs" style="left:31px;top:1172px" width="44" height="44" viewBox="0 0 44 44" aria-hidden="true"><circle cx="22" cy="22" r="21" fill="var(--teal)"/><path d="M13 32 V20 L22 13 L31 20 V32 Z" fill="none" stroke="#fff" stroke-width="2.5"/><rect x="19" y="24" width="6" height="8" fill="#fff"/></svg>
  <p class="abs address">845 Makani Ave #210,<br>Honolulu, HI 96814, United States</p>
  <svg class="abs" style="left:31px;top:1230px" width="44" height="44" viewBox="0 0 44 44" aria-hidden="true"><circle cx="22" cy="22" r="20" fill="none" stroke="var(--teal)" stroke-width="3"/><path d="M15 13 L19 13 L21 18 L18 20 C19 23 21 25 24 26 L26 23 L31 25 L31 29 C24 31 13 20 15 13 Z" fill="var(--teal)"/></svg>
  <p class="abs phone">808-555-0142</p>
  <p class="abs web"><svg width="16" height="16" viewBox="0 0 16 16" aria-hidden="true"><circle cx="8" cy="8" r="7" fill="none" stroke="var(--teal)" stroke-width="1.6"/><path d="M1 8 H15 M8 1 C4 5 4 11 8 15 C12 11 12 5 8 1" fill="none" stroke="var(--teal)" stroke-width="1.4"/></svg>www.brantleycare.com</p>

  <svg class="abs" style="left:505px;top:1218px" width="44" height="78" viewBox="0 0 44 78" aria-hidden="true"><rect x="2" y="2" width="40" height="74" rx="6" fill="none" stroke="#fff" stroke-width="2.5"/><path d="M2 12 H42 M2 64 H42" stroke="#fff" stroke-width="2"/><rect x="11" y="30" width="22" height="16" fill="none" stroke="#fff" stroke-width="2"/><path d="M11 30 L22 40 L33 30" fill="none" stroke="#fff" stroke-width="2"/></svg>
  <div class="abs apply">
    <p class="apply-lead">Please send your Applications at</p>
    <p class="apply-mail">recruitment@brantleycare.com</p>
  </div>
</main>
</body>
</html>
```